CraneHollow - Business Card and Letterhead

After having received some fantastic submissions in our recent logo design project, I would now like to extend our branding to letterheads and business cards.
CraneHollow is a consulting service in the Construction Industry. We deal with both residential and commercial projects, and our clients include Architects, Builders, Tradespeople and Home Owners.
The designs should be simple and effective, convey personal service and professionalism, and display some level of creativity.
For both the business cards and letterhead, a white card stock will be used. This project is for business cards and letterheads only. Our new logo is attached for use.
The designs should incorporate our two main colours which are Blue (RGB 14,92,143) and Green (RGB 132,194,37).
For the time being, please submit all designs showing generic information including name, mobile number, email, postal address and website details. No fax number or physical address is required. I will provide our actual contact details once a final design has been selected.
I encourage you to interpret this brief in your own creative way, and look forward to some quality submissions.
Thanks!
Leo
CraneHollow.

```html
<!DOCTYPE html>
<html lang="en">
<head>
<meta charset="utf-8">
<title>CraneHollow – Business Card</title>
<link rel="stylesheet" href="https://fonts.googleapis.com/css2?family=Open+Sans:wght@700&family=Questrial&display=swap">
<style>
  :root {
    --brand-blue: #0e5c8f;
    --brand-green: #84c225;
    --card-white: #fbfbfb;
    --ink-grey: #4a4a4a;
    --text-grey: #555555;
    --backdrop: #e6e8eb;
  }
  * { box-sizing: border-box; margin: 0; padding: 0; }
  html, body { width: 1200px; height: 800px; overflow: hidden; }
  body {
    background: var(--backdrop);
    display: flex;
    align-items: center;
    justify-content: center;
    gap: 60px;
    font-family: "Questrial", "Century Gothic", sans-serif;
  }
  .card {
    position: relative;
    width: 520px;
    height: 318px;
    border-radius: 4px;
    overflow: hidden;
    box-shadow: 0 6px 18px rgba(0,0,0,0.18);
  }
  .card-front { background: var(--card-white); }
  .card-back {
    background: var(--brand-blue);
    display: flex;
    align-items: center;
    justify-content: center;
  }
  .wordmark {
    display: flex;
    align-items: center;
    gap: 10px;
    font-family: "Open Sans", Arial, sans-serif;
    font-weight: 700;
    letter-spacing: -0.5px;
  }
  .wordmark-mark { display: block; border-radius: 3px; }
  .card-front .wordmark {
    position: absolute;
    left: 34px;
    top: 38px;
    font-size: 38px;
    color: var(--brand-blue);
  }
  .card-front .wordmark-mark { width: 30px; height: 30px; background: var(--brand-green); }
  .card-back .wordmark { font-size: 42px; color: #ffffff; }
  .card-back .wordmark-mark { width: 32px; height: 32px; background: var(--brand-green); }
  .holder-name {
    position: absolute;
    right: 34px;
    top: 186px;
    font-family: "Open Sans", Arial, sans-serif;
    font-weight: 700;
    font-size: 22px;
    letter-spacing: 0.3px;
    color: var(--ink-grey);
  }
  .contact {
    position: absolute;
    left: 34px;
    top: 222px;
    font-size: 13.5px;
    line-height: 1.45;
    color: var(--text-grey);
    list-style: none;
  }
  .contact-label { color: var(--brand-blue); font-weight: 700; }
  .contact-gap { margin-left: 8px; }
  .card-bands { position: absolute; left: 0; bottom: 0; width: 520px; height: 44px; }
</style>
</head>
<body>
  <article class="card card-front">
    <div class="wordmark">
      <span class="wordmark-mark"></span>
      <span class="wordmark-name">CraneHollow</span>
    </div>
    <p class="holder-name">NORA QUILL</p>
    <ul class="contact">
      <li>27 Harbour Lane, Eastmere NSW 2410</li>
      <li><span class="contact-label">M:</span> 0400 123 456<span class="contact-gap"><span class="contact-label">E:</span> quill@cranehollow.com</span></li>
      <li>www.cranehollow.com</li>
    </ul>
    <svg class="card-bands" viewBox="0 0 520 44" aria-hidden="true">
      <polygon points="300,26 318,4 520,4 520,26" fill="var(--brand-green)"/>
      <polygon points="0,30 300,26 520,26 520,44 0,44" fill="var(--brand-blue)"/>
    </svg>
  </article>

  <article class="card card-back">
    <div class="wordmark">
      <span class="wordmark-mark"></span>
      <span class="wordmark-name">CraneHollow</span>
    </div>
  </article>
</body>
</html>
```